HI, I would like a flyer design for out Harbor Glow series. Details are:
- To be full colour
- 210mm wide x 100mm deep
- Finished file to be a print-ready (for gloss paper) layered .psd file.

**I am open to buying PixVault images, but please use a positional in initial designs until approval**

Target Market(s)

18 - 35 year old people looking for fun and connection

Requirements
Must have
• - Chapel522 Logo

Text:
Chapel522 (logo) presents
Harbor Glow (Heading)

Awesome Summer Series on Sunday nights January 8, 15, 22 and 29 at 6pm - Followed by a FREE BBQ!
Fore more information, contact 4613 5720, email info@chapel522.example, www.chapel522.example, www.socialsite.example/brightwayforward (Body)

Chapel522 - The Mariner, 412 Quill Road, Newcastle

Must Include:
- Beach and Sun
Nice to have
• beachballs, surfboards, waves/water, people having fun in the sun and on the beach, beach umbrellas, colourful beach balls a shark tower/lifesaver tower with life saver rings and beach towels etc...

So colourful, beach and fun,
Should not have
• - Any photos etc. showing obscene amounts of skin.
- no sand castles

```html
<!DOCTYPE html>
<html lang="en">
<head>
<meta charset="utf-8">
<title>Harbor Glow flyers</title>
<link rel="stylesheet" href="https://fonts.googleapis.com/css2?family=Arimo:wght@400;700&family=Roboto+Condensed:wght@700&family=Yellowtail&display=swap">
<style>
:root{
  --navy:#1e3466;
  --navy-dark:#152850;
  --teal:#0f6a8f;
  --sky:#2a8fc6;
  --white:#ffffff;
  --ink:#111111;
  --silver-light:#f4f4f5;
  --silver-mid:#c9cacd;
  --silver-dark:#8e9095;
  --sand:#dbc4a8;
  --sand-light:#e9d9c5;
  --frame:#000000;
}
*{margin:0;padding:0;box-sizing:border-box}
html,body{width:1200px;height:741px;overflow:hidden;background:var(--white)}
.canvas{position:relative;width:1200px;height:741px;font-family:"Arimo",Arial,sans-serif}
.flyer{position:absolute;width:624px;height:300px;border:5px solid var(--frame);overflow:hidden;background:var(--silver-light)}
.flyer--beach{left:59px;top:49px}
.flyer--surf{left:266px;top:376px}
.abs{position:absolute}
.photo{position:absolute}
.heading{font-family:"Yellowtail",cursive;color:var(--navy);white-space:nowrap;overflow:visible;
  text-shadow:
   2px 0 0 var(--white),-2px 0 0 var(--white),0 2px 0 var(--white),0 -2px 0 var(--white),
   2px 2px 0 var(--white),-2px -2px 0 var(--white),2px -2px 0 var(--white),-2px 2px 0 var(--white),
   4px 0 0 var(--navy),-4px 0 0 var(--navy),0 4px 0 var(--navy),0 -4px 0 var(--navy),
   3px 3px 0 var(--navy),-3px -3px 0 var(--navy),3px -3px 0 var(--navy),-3px 3px 0 var(--navy)}
.series{color:var(--navy);font-weight:700;white-space:nowrap}
.band{position:absolute;left:0}
.band--silver{background:linear-gradient(180deg,var(--silver-light),var(--silver-mid) 50%,var(--silver-dark))}
.band--navy{background:var(--navy)}
.dates{color:var(--white);font-weight:700;letter-spacing:1px;white-space:nowrap}
.month{color:var(--white);font-weight:700;white-space:nowrap}
.divider{position:absolute;width:1.5px;background:var(--white)}
.nights{font-family:"Roboto Condensed",Arial,sans-serif;color:var(--white);font-weight:700;white-space:nowrap}
.bbq{color:var(--white);white-space:nowrap}
.bbq b{font-weight:700;letter-spacing:.5px}
.sand{position:absolute;left:0;right:0;bottom:0;background:linear-gradient(100deg,var(--sand) 0%,var(--sand-light) 55%,var(--sand) 100%)}
.info-title{color:var(--ink);white-space:nowrap}
.info-box{position:absolute;border:1.5px solid var(--ink);border-radius:2px;overflow:hidden}
.info-box p{color:var(--ink);white-space:nowrap;line-height:1.35}
.address{color:var(--ink);font-weight:700;white-space:nowrap}
.brand{color:var(--navy);font-weight:700;white-space:nowrap;letter-spacing:.5px}
.presents{color:var(--ink);font-weight:700;white-space:nowrap}
</style>
</head>
<body>
<div class="canvas">

  <!-- Landscape flyer: photo strip on top -->
  <section class="flyer flyer--beach">
    <div class="photo" style="left:0;top:0;width:177px;height:137px;background:linear-gradient(180deg,#2f5fa8 0%,#6f9fd4 45%,#38b3c4 65%,#e8dcc2 100%)" role="img" aria-label="Tropical beach with a striped umbrella under a blue sky"></div>
    <div class="photo" style="left:177px;top:0;width:225px;height:137px;background:linear-gradient(160deg,#e4c8ab,#d7b08f 60%,#c89d7e)" role="img" aria-label="Friends playing beach volleyball on the sand, seen from above"></div>
    <div class="photo" style="left:402px;top:0;width:212px;height:137px;background:linear-gradient(180deg,#f2efe9 0%,#d9d3c4 55%,#c6bba6 100%)" role="img" aria-label="Pale green flip-flops with yellow daisies on sand"></div>

    <div class="band band--silver" style="top:137px;width:614px;height:17px"></div>
    <div class="band band--navy" style="top:154px;width:614px;height:19px"></div>
    <div class="band band--silver" style="top:173px;width:614px;height:7px"></div>
    <div class="band band--navy" style="top:180px;width:614px;height:17px"></div>
    <div class="band band--silver" style="top:197px;width:614px;height:13px"></div>

    <div class="heading abs" style="left:132px;top:78px;height:58px;font-size:60px;line-height:58px">Harbor Glow</div>
    <div class="series abs" style="left:419px;top:138px;font-size:13.5px">Awesome Summer Series</div>

    <div class="dates abs" style="left:149px;top:157px;font-size:12px">8, 15, 22 &amp; 29</div>
    <div class="month abs" style="left:276px;top:150px;font-size:24px">January</div>
    <div class="divider" style="left:401px;top:155px;height:20px"></div>
    <div class="month abs" style="left:410px;top:150px;font-size:24px">6pm</div>
    <div class="nights abs" style="left:156px;top:181px;font-size:13px">Sunday nights</div>
    <div class="bbq abs" style="left:275px;top:182px;font-size:12.5px">Followed by a <b>FREE BBQ!</b></div>

    <div class="sand" style="top:210px"></div>
    <div class="info-title abs" style="left:25px;top:215px;font-size:10.5px">For more information :</div>
    <div class="info-box" style="left:25px;top:229px;width:208px;height:57px;padding:4px 0 0 14px">
      <p style="font-size:8.5px">contact : 4613 5720</p>
      <p style="font-size:8.5px">email &nbsp;&nbsp;: info@chapel522.example</p>
      <p style="font-size:8.5px">www.socialsite.example/brightwayforward</p>
      <p style="font-size:8.5px">www.chapel522.example</p>
    </div>
    <div class="address abs" style="left:242px;top:258px;font-size:7.5px">The Mariner, 412 Quill Road, Newcastle</div>
    <div class="brand abs" style="left:432px;top:254px;font-size:14px">Chapel522</div>
    <div class="presents abs" style="left:550px;top:257px;font-size:10.5px">Presents</div>
  </section>

  <!-- Landscape flyer: diagonal stripes with wave photo -->
  <section class="flyer flyer--surf">
    <div class="abs" style="left:0;top:0;width:614px;height:290px;background:linear-gradient(180deg,var(--white) 0%,var(--silver-light) 30%,var(--silver-mid) 100%)"></div>

    <div class="brand abs" style="left:137px;top:10px;font-size:14px;line-height:16px">Chapel522</div>
    <div class="presents abs" style="left:256px;top:12px;font-size:10.5px;line-height:14px">Presents</div>
    <div class="heading abs" style="left:40px;top:36px;height:56px;font-size:56px;line-height:56px">Harbor Glow</div>
    <div class="series abs" style="left:54px;top:98px;font-size:13.5px">Awesome Summer Series</div>

    <div class="band" style="top:121px;width:420px;height:16px;background:linear-gradient(90deg,var(--navy) 0 215px,var(--sky) 215px,#4aa5d8)"></div>
    <div class="band band--navy" style="top:137px;width:420px;height:16px"></div>
    <div class="band" style="top:153px;width:420px;height:32px;background:linear-gradient(90deg,var(--teal) 0 135px,var(--sky) 135px,#5fb6e2)"></div>
    <div class="band band--silver" style="top:185px;width:420px;height:5px"></div>

    <div class="dates abs" style="left:22px;top:138px;font-size:12px">8, 15, 22 &amp; 29</div>
    <div class="month abs" style="left:149px;top:131px;font-size:24px">January</div>
    <div class="divider" style="left:274px;top:134px;height:26px"></div>
    <div class="month abs" style="left:284px;top:133px;font-size:22px">6pm</div>
    <div class="nights abs" style="left:29px;top:163px;font-size:13px">Sunday nights</div>
    <div class="bbq abs" style="left:148px;top:164px;font-size:12.5px">Followed by a <b>FREE BBQ!</b></div>

    <div class="sand" style="top:190px"></div>
    <div class="info-title abs" style="left:24px;top:199px;font-size:10.5px">For more information :</div>
    <div class="info-box" style="left:23px;top:215px;width:172px;height:49px;padding:4px 0 0 10px">
      <p style="font-size:7px">contact : 4613 5720</p>
      <p style="font-size:7px">email &nbsp;&nbsp;: info@chapel522.example</p>
      <p style="font-size:7px">www.socialsite.example/brightwayforward</p>
      <p style="font-size:7px">www.chapel522.example</p>
    </div>
    <div class="address abs" style="left:22px;top:276px;font-size:7.5px">Chapel522 - The Mariner, 412 Quill Road, Newcastle</div>

    <svg class="abs" style="left:0;top:0" width="614" height="290" viewBox="0 0 614 290" aria-hidden="true">
      <defs>
        <linearGradient id="wave-tones" x1="0" y1="0" x2="1" y2="1">
          <stop offset="0" stop-color="#0b4f8c"/>
          <stop offset=".5" stop-color="#2a9bd0"/>
          <stop offset="1" stop-color="#cfe9f5"/>
        </linearGradient>
        <linearGradient id="stripe-silver" x1="0" y1="0" x2="1" y2="0">
          <stop offset="0" stop-color="#f4f4f5"/>
          <stop offset=".5" stop-color="#bfc1c5"/>
          <stop offset="1" stop-color="#ffffff"/>
        </linearGradient>
      </defs>
      <polygon points="497,0 525,0 221,290 193,290" fill="url(#stripe-silver)"/>
      <polygon points="525,0 561,0 257,290 221,290" fill="var(--navy)"/>
      <polygon points="561,0 569,0 265,290 257,290" fill="var(--white)"/>
      <polygon points="569,0 592,0 288,290 265,290" fill="var(--navy)"/>
      <polygon points="592,0 614,0 614,290 288,290" fill="url(#wave-tones)" role="img" aria-label="Surfer riding inside a curling blue wave"/>
    </svg>
  </section>

</div>
</body>
</html>
```